Cleaning services Business Card Design

I need a business card design for my Cleaning business. I would like perhaps emphasis on the company name, Muddle to Marvel. Maybe the Muddle would to dirty and the marvel would have sprinkles.

Industry/Entity Type

Business

Contact Information for Business Card

Muddle to Marvel Cleaning Services, Tomas Ordell, Industrial, Commercial, & Residential 415-806-2147

```html
<!DOCTYPE html>
<html lang="en">
<head>
<meta charset="utf-8">
<title>Muddle to Marvel Cleaning Services – Business Card</title>
<link rel="stylesheet" href="https://fonts.googleapis.com/css2?family=Tinos:wght@400;700&display=swap">
<style>
  :root {
    --backdrop: #8d8d8d;
    --card: #fbfbfa;
    --navy: #1f3a9a;
    --orange: #ee8700;
    --ink: #141414;
    --accent-blue: #2a8fd8;
  }
  * { box-sizing: border-box; margin: 0; padding: 0; }
  html, body {
    width: 1200px; height: 900px; overflow: hidden;
    background: var(--backdrop);
    font-family: "Tinos", "Times New Roman", serif;
  }
  .business-card {
    position: absolute;
    left: 100px; top: 164px;
    width: 1000px; height: 572px;
    background: var(--card);
    box-shadow: 0 14px 30px rgba(0,0,0,.25);
    overflow: hidden;
  }
  .brand {
    position: absolute;
    left: 90px; top: 70px;
    display: flex; align-items: flex-start; gap: 26px;
  }
  .brand-dot {
    width: 92px; height: 92px; border-radius: 50%;
    background: var(--accent-blue);
    flex: none;
  }
  .brand-text { padding-top: 8px; }
  .brand-name {
    color: var(--navy);
    font-size: 58px; font-weight: 400;
    text-transform: uppercase;
    line-height: 1;
    letter-spacing: 1px;
  }
  .brand-name .services {
    display: block;
    font-size: 27px;
    letter-spacing: 10px;
    margin-top: 2px;
    padding-bottom: 4px;
    border-bottom: 2px solid var(--navy);
  }
  .tagline {
    color: var(--orange);
    font-size: 21px;
    text-transform: uppercase;
    letter-spacing: 2px;
    margin-top: 6px;
  }
  .contact {
    position: absolute;
    left: 90px; top: 300px;
  }
  .contact-name { color: var(--ink); font-size: 34px; line-height: 1.05; }
  .contact-role { color: var(--orange); font-size: 20px; line-height: 1.2; }
  .contact-phone {
    display: flex; align-items: center; gap: 8px;
    color: var(--ink); font-size: 24px; margin-top: 2px;
  }
  .phone-icon { width: 18px; height: 18px; }
  .swoosh { position: absolute; inset: 0; width: 1000px; height: 572px; }
</style>
</head>
<body>
  <div class="business-card">
    <svg class="swoosh" viewBox="0 0 1000 572" aria-hidden="true">
      <path d="M380 572 Q620 420 1000 395 L1000 572 Z" fill="var(--navy)"/>
      <path d="M380 572 Q660 455 1000 442 L1000 572 Z" fill="var(--orange)"/>
    </svg>

    <div class="brand">
      <div class="brand-dot"></div>
      <div class="brand-text">
        <h1 class="brand-name">Muddle to Marvel<span class="services">Cleaning Services</span></h1>
        <p class="tagline">Industrial, Commercial, &amp; Residential</p>
      </div>
    </div>

    <div class="contact">
      <p class="contact-name">Tomas Ordell</p>
      <p class="contact-role">Owner</p>
      <p class="contact-phone">
        <svg class="phone-icon" viewBox="0 0 18 18" aria-hidden="true">
          <rect width="18" height="18" rx="3" fill="var(--navy)"/>
          <path d="M5 4.5c.6-.5 1.3-.4 1.6.2l.9 1.7c.2.5 0 1-.4 1.3l-.6.4c.5 1.2 1.4 2.1 2.6 2.6l.4-.6c.3-.4.8-.6 1.3-.4l1.7.9c.6.3.7 1 .2 1.6-.8.9-2 1.2-3.1.7C7.3 11.9 6.1 10.7 4.8 8.4 4.2 7.2 4.2 5.4 5 4.5z" fill="#fff"/>
        </svg>
        415-806-2147
      </p>
    </div>
  </div>
</body>
</html>
```